Vantrell Law Letterhead

We need a new letterhead design for a Law Firm. The address for the law firm is 4817 Larkspur Boulevard, Suite 250, Houston, Texas 77342. Phone Number: 832-619-3057; Fax Number: 832-407-1694. The logo is uploaded to the project.

```html
<!DOCTYPE html>
<html lang="en">
<head>
<meta charset="utf-8">
<title>Vantrell Law Letterhead</title>
<link href="https://fonts.googleapis.com/css2?family=Crimson+Text:wght@400;600&display=swap" rel="stylesheet">
<style>
  :root {
    --navy: #1f3766;
    --navy-light: #1f4a80;
    --navy-deep: #1c2f5c;
    --red: #e21f27;
    --red-dark: #9c1c24;
    --paper: #ffffff;
  }
  html, body {
    margin: 0;
    padding: 0;
    overflow: hidden;
    background: var(--paper);
  }
  .letterhead {
    position: relative;
    width: 849px;
    height: 1200px;
    overflow: hidden;
    background: var(--paper);
    font-family: "Crimson Text", Georgia, serif;
    color: var(--navy);
  }
  .band {
    position: absolute;
    left: 0;
    width: 849px;
    display: block;
  }
  .band--top { top: 0; height: 52px; }
  .band--bottom { top: 1095px; height: 105px; }

  .brand {
    position: absolute;
    left: 93px;
    top: 128px;
    display: flex;
    align-items: center;
    gap: 14px;
  }
  .brand__mark {
    width: 62px;
    height: 74px;
    background: var(--navy);
  }
  .brand__name {
    font-size: 44px;
    font-weight: 600;
    letter-spacing: 1px;
    color: var(--navy);
    line-height: 1;
  }

  .contact {
    position: absolute;
    top: 1090px;
    left: 0;
    width: 849px;
    height: 44px;
  }
  .contact__item {
    position: absolute;
    display: flex;
    align-items: flex-start;
    gap: 8px;
    font-size: 21px;
    line-height: 19px;
    color: var(--navy);
    white-space: nowrap;
  }
  .contact__item--phone { left: 132px; top: 2px; }
  .contact__item--fax { left: 298px; top: 2px; }
  .contact__item--address { left: 461px; top: 1px; }
  .contact__icon {
    width: 18px;
    height: 18px;
    flex: none;
    margin-top: 1px;
  }
</style>
</head>
<body>
<div class="letterhead">

  <svg class="band band--top" viewBox="0 0 849 52" aria-hidden="true">
    <rect width="849" height="52" fill="var(--navy)"/>
    <polygon points="269,0 580,0 536,52 314,52" fill="var(--navy-light)"/>
    <polygon points="292,0 557,0 513,52 335,52" fill="var(--navy-deep)"/>
    <polygon points="302,0 546,0 503,52 345,52" fill="var(--red-dark)"/>
    <polygon points="316,0 533,0 494,46 354,46" fill="var(--red)"/>
  </svg>

  <header class="brand">
    <div class="brand__mark"></div>
    <div class="brand__name">Vantrell Law</div>
  </header>

  <svg class="band band--bottom" viewBox="0 0 849 105" aria-hidden="true">
    <rect width="849" height="105" fill="var(--navy)"/>
    <path d="M72,0 C100,0 112,10 127,26 C145,45 158,53 178,53 L672,53 C692,53 705,45 722,26 C737,10 750,0 778,0 Z" fill="var(--paper)"/>
    <g transform="translate(0,53)">
      <polygon points="269,0 580,0 536,52 314,52" fill="var(--navy-light)"/>
      <polygon points="292,0 557,0 513,52 335,52" fill="var(--navy-deep)"/>
      <polygon points="302,0 546,0 503,52 345,52" fill="var(--red-dark)"/>
      <polygon points="316,0 533,0 494,46 354,46" fill="var(--red)"/>
    </g>
  </svg>

  <footer class="contact">
    <div class="contact__item contact__item--phone">
      <svg class="contact__icon" viewBox="0 0 18 18" aria-hidden="true">
        <circle cx="9" cy="9" r="9" fill="var(--red-dark)"/>
        <path d="M6.2,4.5 L7.6,6.6 L6.8,7.6 C7.4,8.9 8.6,10.2 10,10.9 L11,10.1 L13.2,11.5 L12.4,13.2 C8.6,13 5,9.4 4.8,5.3 Z" fill="var(--paper)"/>
      </svg>
      <span>832-619-3057</span>
    </div>
    <div class="contact__item contact__item--fax">
      <svg class="contact__icon" viewBox="0 0 18 18" aria-hidden="true">
        <circle cx="9" cy="9" r="9" fill="var(--red-dark)"/>
        <rect x="6" y="4" width="6" height="3" fill="var(--paper)"/>
        <rect x="4" y="7.5" width="10" height="5" rx="1" fill="var(--paper)"/>
        <rect x="6" y="10.5" width="6" height="3.5" fill="var(--paper)" stroke="var(--red-dark)" stroke-width="0.8"/>
      </svg>
      <span>832-407-1694</span>
    </div>
    <div class="contact__item contact__item--address">
      <svg class="contact__icon" viewBox="0 0 18 18" aria-hidden="true">
        <circle cx="9" cy="9" r="9" fill="var(--red-dark)"/>
        <path d="M9,3.5 C6.6,3.5 5,5.2 5,7.3 C5,10 9,14.5 9,14.5 C9,14.5 13,10 13,7.3 C13,5.2 11.4,3.5 9,3.5 Z" fill="var(--paper)"/>
        <circle cx="9" cy="7.3" r="1.6" fill="var(--red-dark)"/>
      </svg>
      <span>4817 Larkspur Boulevard, Suite<br>250, Houston, Texas 77342</span>
    </div>
  </footer>

</div>
</body>
</html>
```